Postcard Design

We need a postcard design for a private lender in the Denver area. We are offering hard money loans and loans for those doing fix-and-flips. We definitely want something that is Colorado-specific, maybe a view of downtown Denver? We are not offering small personal loans, but we are also not lending over 800k. Our audience is not major corporations. all the info in the old postcard is correct EXCEPT:

the new email should be tamberly615@vornelmail.com

We would like to omit all use of exclamation points.

```html
<!DOCTYPE html>
<html lang="en">
<head>
<meta charset="utf-8">
<title>Kestrel Lending Co. – Hard Money Loans Postcard</title>
<link rel="stylesheet" href="https://fonts.googleapis.com/css2?family=Arimo:wght@700&family=Open+Sans:wght@400;700&family=Roboto+Condensed:wght@300;400;700&display=swap">
<style>
  :root {
    --backdrop: #1d2229;
    --paper: #e8e9eb;
    --white: #ffffff;
    --title-teal: #1a8fb5;
    --navy: #1d3f9a;
    --bright-blue: #0a9ee0;
    --cyan: #00b5ec;
    --deep-teal: #1b7fa0;
    --panel-teal: #2196b8;
    --lender-blue: #1d4f9e;
    --money-yellow: #ffd200;
    --phone-red: #e8202a;
    --ink: #111111;
    --green: #76c043;
    --orange: #f7a823;
  }
  * { box-sizing: border-box; margin: 0; padding: 0; }
  html, body { width: 1200px; height: 1200px; overflow: hidden; background: var(--backdrop); }
  .canvas { position: relative; width: 1200px; height: 1200px; }

  .card-front, .card-back { position: absolute; left: 269px; width: 662px; overflow: hidden; }
  .card-front { top: 81px; height: 515px; background: var(--paper); }
  .card-back { top: 606px; height: 513px; background: var(--white); }
  .shapes { position: absolute; inset: 0; width: 100%; height: 100%; }

  .brand-title {
    position: absolute; top: 26px; left: 0; width: 100%; text-align: center;
    font: 700 44px/52px "Roboto Condensed", sans-serif; color: var(--title-teal); letter-spacing: -0.5px;
  }
  .hero-line {
    position: absolute; left: 0; width: 380px; text-align: center;
    font-family: "Arimo", Arial, sans-serif; font-weight: 700; color: var(--white);
  }
  .hero-hard { top: 140px; height: 62px; font-size: 62px; line-height: 62px; }
  .hero-money { top: 203px; height: 86px; font-size: 86px; line-height: 86px; color: var(--money-yellow); }
  .hero-loans { top: 286px; height: 62px; font-size: 62px; line-height: 62px; }

  .offer-list { position: absolute; left: 411px; top: 151px; width: 220px; list-style: none;
    font: 300 17.6px/28px "Roboto Condensed", sans-serif; color: var(--ink); }
  .offer-list li { position: relative; padding-left: 17px; }
  .offer-list li::before { content: ""; position: absolute; left: 0; top: 11px; width: 6px; height: 6px; border-radius: 50%; background: var(--ink); }
  .offer-list li + li { border-top: 1px solid var(--white); margin-top: 6px; padding-top: 6px; }
  .offer-list li + li::before { top: 17px; }
  .offer-list .tight { line-height: 26px; }

  .lender-tag { position: absolute; top: 392px; left: 0; width: 380px; text-align: center;
    font: 700 24px/30px "Roboto Condensed", sans-serif; color: var(--lender-blue); }
  .lender-slogan { position: absolute; top: 428px; left: 0; width: 380px; text-align: center;
    font: 400 22px/28px "Open Sans", sans-serif; color: var(--ink); }
  .lender-call { position: absolute; top: 459px; left: 0; width: 380px; text-align: center;
    font: 700 26px/34px "Open Sans", sans-serif; color: var(--ink); }
  .lender-call .phone { color: var(--phone-red); }

  .contact { position: absolute; left: 418px; top: 427px;
    font: 400 18px/30px "Roboto Condensed", sans-serif; color: var(--ink); }

  .back-brand { position: absolute; left: 42px; top: 28px;
    font: 700 22px/26px "Roboto Condensed", sans-serif; color: var(--white); }
  .back-address { position: absolute; left: 42px; top: 55px;
    font: 400 18px/24px "Roboto Condensed", sans-serif; color: var(--white); }
  .ribbon-text { font-family: "Roboto Condensed", sans-serif; font-weight: 700; fill: var(--ink); }
</style>
</head>
<body>
<main class="canvas">

  <section class="card-front">
    <svg class="shapes" viewBox="0 0 828 644" preserveAspectRatio="none" aria-hidden="true">
      <defs>
        <linearGradient id="heroBlue" x1="0" x2="1" y1="0" y2="0">
          <stop offset="0" stop-color="#1d3f9a"/>
          <stop offset="1" stop-color="#0a9ee0"/>
        </linearGradient>
      </defs>
      <polygon points="459,130 828,130 828,511 459,511 419,475 419,167" fill="var(--cyan)"/>
      <polygon points="0,167 429,167 489,319 429,475 0,475" fill="url(#heroBlue)"/>
      <rect x="0" y="632" width="828" height="12" fill="var(--deep-teal)"/>
    </svg>

    <h1 class="brand-title">Kestrel Lending Co.</h1>

    <div class="hero-line hero-hard">Hard</div>
    <div class="hero-line hero-money">MONEY</div>
    <div class="hero-line hero-loans">Loans</div>

    <ul class="offer-list">
      <li>We do a variety of real estate secured loans including loans to buy foreclosures, short sales &amp; more.</li>
      <li>Fix &amp; flip Loans at 10%</li>
      <li class="tight">No appraisal, processing fees or “junk” fees</li>
    </ul>

    <p class="lender-tag">Denver Private Money Lender</p>
    <p class="lender-slogan">Private money for less</p>
    <p class="lender-call">call us at <span class="phone">303-555-0147</span></p>

    <p class="contact">tamberly615@vornelmail.com<br>www.kestrellending.com</p>
  </section>

  <section class="card-back">
    <svg class="shapes" viewBox="0 0 828 641" preserveAspectRatio="none">
      <rect x="0" y="0" width="400" height="641" fill="var(--panel-teal)"/>
      <polygon points="0,273 400,171 400,235 0,335" fill="var(--green)"/>
      <polygon points="0,335 400,235 400,303 0,403" fill="var(--cyan)"/>
      <polygon points="0,403 400,303 400,367 0,469" fill="var(--orange)"/>
      <text class="ribbon-text" x="171" y="263" font-size="50" text-anchor="middle" dominant-baseline="central" transform="rotate(-14 171 263)">LOW COST</text>
      <text class="ribbon-text" x="189" y="328" font-size="55" text-anchor="middle" dominant-baseline="central" transform="rotate(-14 189 328)">HARD MONEY</text>
      <text class="ribbon-text" x="205" y="390" font-size="45" text-anchor="middle" dominant-baseline="central" transform="rotate(-14 205 390)">REAL ESTATE LOANS</text>
    </svg>
    <p class="back-brand">Kestrel Lending Co.</p>
    <p class="back-address">2417 Larkmoor St<br>Denver, CO 80205</p>
  </section>

</main>
</body>
</html>
```